New template needed for Joomla 3.2 website

We are a mortgage origination company based in Johannesburg, South Africa and require a sleek, modern & professional look for our website.
The website is complete and your template should accommodate all pages on the site (there are not many) and be ready for Joomla implementation.
Our website can be viewed at www.keystonelending.example.co.za
Target Market(s)
We are targeting consumers who require mortgage finance to buy real estate. There is no particular demographic, except that we cater to South African home buyers exclusively!
Requirements
Must have
- It must look professional and modern.
Take a look at competitor websites:
www.vundo.example.co.za
www.zqbondhub.example.com
http://www.brightpathfold.example.co.za/loanpeak/
http://www.tideloan.example.co.za/
We want to beat the competition !!
Nice to have
- Website should blend with company logo and play on the symbol in the logo.
I want more of a people / photo element to the template. It needs to make us seem "tangible"

```html
<!DOCTYPE html>
<html lang="en">
<head>
<meta charset="utf-8">
<title>Keystone Lending</title>
<link href="https://fonts.googleapis.com/css2?family=Open+Sans:wght@300;400;600;700&display=swap" rel="stylesheet">
<style>
:root{
  --blue:#0d58a6;
  --blue-dark:#0a3f7a;
  --nav-top:#1a72c9;
  --nav-bottom:#0b56a3;
  --gold:#f2c21b;
  --ink:#333;
  --muted:#777;
  --rule:#dcdcdc;
  --panel:#eef3f8;
  --foot:#f2f2f2;
  --foot-dark:#262626;
  --btn:#e3ebf3;
  --social:#8a9bb0;
}
*{margin:0;padding:0;box-sizing:border-box}
html,body{width:836px;height:1200px;overflow:hidden;background:#fff}
body{font-family:"Open Sans",Arial,sans-serif;color:var(--ink);position:relative}
.abs{position:absolute}

/* header */
.brand-name{left:70px;top:27px;font-size:26px;font-weight:600;color:var(--blue);line-height:32px}
.phone{right:70px;top:34px;font-size:14px;color:#888;display:flex;align-items:center;gap:6px}
.phone strong{color:var(--blue);font-weight:600}

/* nav */
.nav{left:0;top:88px;width:836px;height:35px;background:linear-gradient(var(--nav-top),var(--nav-bottom))}
.nav ul{list-style:none;display:flex;margin-left:70px;height:35px}
.nav li{font-size:10.5px;font-weight:600;color:#fff;padding:0 13px;line-height:35px;border-right:1px solid rgba(0,0,0,.25)}
.nav li.active{background:var(--blue-dark)}

/* hero */
.hero{left:0;top:123px;width:836px;height:340px}
.hero-photo{position:absolute;inset:0;background:linear-gradient(100deg,#ece7de 0%,#d9d2c6 35%,#c8c2ba 60%,#e4e4e6 100%)}
.hero-panel{position:absolute;left:578px;top:0;width:189px;height:340px;background:rgba(40,40,40,.93);padding:0 11px 0 15px}
.feature{padding:22px 0 20px;border-bottom:1px solid #666}
.feature:last-child{border-bottom:none}
.feature h3{font-size:14.5px;font-weight:600;color:var(--gold);margin-bottom:6px}
.feature p{font-size:9.3px;line-height:14.5px;color:#ccc}
.arrow{position:absolute;top:147px;width:36px;height:46px;background:rgba(120,120,120,.55)}

/* lenders */
.lenders{left:0;top:490px;width:836px;text-align:center}
.lenders h2{font-size:19px;font-weight:600;color:var(--blue)}
.lenders p{font-size:11.5px;color:#555;margin-top:4px;letter-spacing:.2px}
.rule{left:70px;width:697px;height:1px;background:var(--rule)}

.tagline{left:0;top:574px;width:836px;text-align:center;font-size:27px;font-weight:300;color:#999}

/* services */
.services{left:70px;top:625px;width:697px;display:flex}
.service{flex:1;text-align:center}
.service svg{height:24px}
.service h4{font-size:13.5px;font-weight:600;color:var(--blue);margin-top:12px}
.service p{font-size:9px;line-height:13.5px;color:var(--muted);margin:6px auto 0;width:145px}
.btn{display:inline-block;margin-top:10px;background:var(--btn);font-size:10px;color:#333;padding:5px 11px;border-radius:2px}

/* info boxes */
.info{top:802px;width:344px;height:112px;background:var(--panel);padding:14px 16px}
.info h3{font-size:15.5px;font-weight:600;color:var(--blue);margin-bottom:9px}
.info p{font-size:9.5px;line-height:14.5px;color:#444}

/* footer */
.footer{left:0;top:949px;width:836px;height:175px;background:var(--foot)}
.col{top:18px}
.col h5{font-size:12px;font-weight:400;color:#333;margin-bottom:14px}
.divider{top:18px;width:1px;height:143px;background:#ccc}
.about p{font-size:9px;line-height:14.5px;color:#888;width:170px}
.about a{font-size:9px;color:#1a8ad3;text-decoration:none;display:block;margin-top:6px}
.tweet{background:#fff;width:202px;padding:8px 12px 10px}
.tweet .who{font-size:9.5px;color:#1a8ad3}
.tweet .who span{color:#999}
.tweet p{font-size:9px;line-height:13px;color:#333;margin-top:6px}
.tweet p em{font-style:normal;color:#1a8ad3}
.compose{width:202px;height:30px;border:1px solid #ddd;background:#fff;margin-top:3px;font-size:9px;color:#aaa;padding:8px 12px}
.field{width:144px;height:20px;border:1px solid #ccc;background:#fff;font-size:8px;color:#444;padding:4px 11px;margin-bottom:10px}
.submit{margin-left:94px;width:50px;height:20px;background:#555;color:#fff;font-size:10px;font-weight:600;text-align:center;line-height:20px;border-radius:2px}
.social{left:724px;top:22px;display:flex;flex-direction:column;gap:11px}
.social span{width:24px;height:24px;border-radius:50%;display:flex;align-items:center;justify-content:center;background:var(--social)}
.social span.mail{background:#4f9a3a}

.legal{left:0;top:1124px;width:836px;height:76px;background:var(--foot-dark);text-align:center}
.legal nav{font-size:9px;color:#ccc;margin-top:21px}
.legal nav i{font-style:normal;margin:0 8px}
.legal p{font-size:9px;color:#ccc;margin-top:14px}
</style>
</head>
<body>

<header>
  <div class="abs brand-name">Keystone Lending</div>
  <div class="abs phone">
    <svg width="12" height="12" viewBox="0 0 24 24"><path fill="#999" d="M6.6 10.8a15.1 15.1 0 0 0 6.6 6.6l2.2-2.2a1 1 0 0 1 1-.25 11.4 11.4 0 0 0 3.6.6 1 1 0 0 1 1 1V20a1 1 0 0 1-1 1A17 17 0 0 1 3 4a1 1 0 0 1 1-1h3.5a1 1 0 0 1 1 1c0 1.25.2 2.45.6 3.6a1 1 0 0 1-.25 1z"/></svg>
    Call us <strong>(010) 555 0148</strong>
  </div>
</header>

<nav class="abs nav">
  <ul>
    <li class="active">HOME</li>
    <li>ABOUT KEYSTONE</li>
    <li>IMPORTANT INFORMATION</li>
    <li>HOMELOAN CALCUALTOR</li>
    <li>APPLY ON-LINE</li>
    <li>CONTACT KEYSTONE</li>
  </ul>
</nav>

<section class="abs hero">
  <div class="hero-photo" role="img" aria-label="Photo of a smiling couple on a sofa shaking hands with a home loan consultant"></div>
  <div class="arrow" style="left:0"><svg width="36" height="46"><path d="M23 10 12 23l11 13" stroke="#fff" stroke-width="1.5" fill="none"/></svg></div>
  <div class="arrow" style="right:0"><svg width="36" height="46"><path d="M13 10l11 13-11 13" stroke="#fff" stroke-width="1.5" fill="none"/></svg></div>
  <div class="hero-panel">
    <div class="feature"><h3>100% FREE OF CHARGE</h3><p>No hidden costs or service charges. Our fee is not hidden within the finance charges of your homeloan.</p></div>
    <div class="feature"><h3>EXCEPTIONAL SERVICE</h3><p>No hidden costs or service charges. Our fee is not hidden within the finance charges of your homeloan.</p></div>
    <div class="feature"><h3>CREDIT HELP</h3><p>No hidden costs or service charges. Our fee is not hidden within the finance charges of your homeloan.</p></div>
  </div>
</section>

<section class="abs lenders">
  <h2>WE RAISE YOUR HOMELOAN WITH :</h2>
  <p>NORTHBANK . VELDBANK . KAROO . CAPE TRUST . ZQ BONDHUB . MRT . LIMPOVEST</p>
</section>
<div class="abs rule" style="top:558px"></div>

<h2 class="abs tagline">FAST HOMELOANS . GREAT SERVICE !</h2>

<section class="abs services">
  <div class="service">
    <svg viewBox="0 0 24 24" width="24"><rect x="3" y="4" width="18" height="17" fill="none" stroke="#0d58a6" stroke-width="2"/><rect x="3" y="4" width="18" height="4" fill="#0d58a6"/><path d="M7 2v4M17 2v4M7 11h2M11 11h2M15 11h2M7 15h2M11 15h2M15 15h2" stroke="#0d58a6" stroke-width="2"/></svg>
    <h4>REFERRAL PROGRAM</h4>
    <p>Click on the button below to join our lead referal program and start earning money.</p>
    <span class="btn">Join Today</span>
  </div>
  <div class="service">
    <svg viewBox="0 0 24 24" width="24"><rect x="2" y="10" width="5" height="11" fill="#0d58a6"/><path d="M8 10l4-7c2 0 2.5 1.5 2 4h6a2 2 0 0 1 2 2.3l-1.4 9A2 2 0 0 1 18.6 21H8z" fill="#0d58a6"/></svg>
    <h4>GET PRE QUALIFIED</h4>
    <p>Click on the button below to join our lead referal program and start earning money.</p>
    <span class="btn">Apply Now</span>
  </div>
  <div class="service">
    <svg viewBox="0 0 24 24" width="24"><path d="M7 8a5 5 0 1 1 7 4.6c-1.4.7-2 1.5-2 3V16" fill="none" stroke="#0d58a6" stroke-width="3"/><rect x="10.5" y="19" width="3" height="3" fill="#0d58a6"/></svg>
    <h4>ASK A QUESTION</h4>
    <p>Click on the button below to join our lead referal program and start earning money.</p>
    <span class="btn">Ask Now</span>
  </div>
  <div class="service">
    <svg viewBox="0 0 24 24" width="24"><rect x="4" y="2" width="16" height="20" fill="none" stroke="#0d58a6" stroke-width="2"/><rect x="7" y="5" width="10" height="4" fill="#0d58a6"/><path d="M7 12h2M11 12h2M15 12h2M7 15.5h2M11 15.5h2M15 15.5h2M7 19h2M11 19h2M15 19h2" stroke="#0d58a6" stroke-width="2"/></svg>
    <h4>CALCULATORS</h4>
    <p>Click on the button below to join our lead referal program and start earning money.</p>
    <span class="btn">Calculate</span>
  </div>
</section>
<div class="abs rule" style="top:790px"></div>

<article class="abs info" style="left:70px">
  <h3>Keystone Lead Referral Program</h3>
  <p>We invite members of the public, estate agents, attorneys, property developers and all other property professionals to refer leads to us. Why not join our referal program and earn money for every successful lead. It pays!</p>
</article>
<article class="abs info" style="left:423px">
  <h3>Keystone Rewards Card</h3>
  <p>All members of our lead referal program will receive a Keystone Lending rewards card. We will load money earned from referals to your card and for you to spend in any way you please! These cards are accepted in all retail stores and restaurants.</p>
</article>

<footer class="abs footer">
  <div class="abs col about" style="left:88px">
    <h5>About Us</h5>
    <p>Maecenas quam lacus, facilisis at enim a, sodales aliquam nibh. Ut vehicula, sem id sollicitudin condimentum, diam nisi elementum libero, sed pellentesque felis tellus ut augue. Phasellus a aliquet urna. Integer bibendum.</p>
    <a>Know more</a>
  </div>
  <div class="abs divider" style="left:274px"></div>
  <div class="abs col" style="left:292px">
    <h5 style="margin-left:7px">Latest Tweets</h5>
    <div class="tweet">
      <div class="who">Mark Dube <span>@keystonelending</span></div>
      <p>Nulla tincidunt elit a mauris pulvinar molestie. <em>Nulla suscipit lacus arcu</em>, ac rutrum tellus feugiat sit amet. Ut dictum.</p>
    </div>
    <div class="compose">Compose new Tweet</div>
  </div>
  <div class="abs divider" style="left:510px"></div>
  <div class="abs col" style="left:533px">
    <h5>Email Signup</h5>
    <div class="field">Name</div>
    <div class="field">Email ID</div>
    <div class="submit">SUBMIT</div>
  </div>
  <div class="abs divider" style="left:702px"></div>
  <div class="abs social">
    <span aria-label="Social profile"></span>
    <span aria-label="Social profile"></span>
    <span aria-label="Video channel"></span>
    <span class="mail" aria-label="Email us"><svg width="12" height="9" viewBox="0 0 12 9"><rect width="12" height="9" rx="1" fill="#fff"/><path d="M0.5 0.8 6 5 11.5 0.8" stroke="#4f9a3a" fill="none"/></svg></span>
  </div>
</footer>

<div class="abs legal">
  <nav>Home<i>|</i>About Keystone<i>|</i>Important Information<i>|</i>Homeloan Calcualtor<i>|</i>Apply On-Line<i>|</i>Contact Keystone</nav>
  <p>Copyright © 2014 &nbsp;Keystone Lending. &nbsp;All rights reserved.</p>
</div>

</body>
</html>
```